QBrook718 Business Card Design

I am in need of a business card design.

Business Name: Harbor Stone 718 or Qbrook718 (we can try the business card with both variations)

I would like it to be somewhat different from the "average" business card

What do we do?

We link up with distributors of different items and we Market their products, sell their products, fulfill the shipment, and handle all customer service that goes along with it.

I will be uploading our logo as well as other business card ideas that i have seen and liked on the web.

I like the style of the "graphic design" business card that i uploaded. I was thinking maybe something like that but instead would read.

SYNC | SELL | SHIP

With maybe:
a computer or a Sync icon underneath SYNC
Some form of money sign underneath Sell
a delivery truck or something underneath SHIP.

And then I was thinking maybe put the logo on the back side like in the other business card that i uploaded.

I definitely want a double sided business card.

These are only my suggestions and if i was very confident in my idea then I wouldn't have to be on here. (So make what you think is nice because my opinion is probably not so great anyway!!)

Everything can be changed.

ALSO, For the logo
We can try and remove the text multi channel selling

For the Business card contact info:
Tom Haskins
CEO
2419 Pelkey Avenue
J7R-2B8
Montreal, Quebec

Thanks

Target Market(s)

Businesses

Industry/Entity Type

Information Technology

Font styles to use
Serif
Sans Serif
Decorative

Colors
34a6d6
33b8a4
aaaaaa
85cae6
33a6d7
0492cd
9d9d9d

Requirements
Must have
• Double Sided Business card
Nice to have
• Illustration graphics / Icons underneath the main points

```html
<!DOCTYPE html>
<html lang="en">
<head>
<meta charset="utf-8">
<title>QBrook718 Business Card</title>
<link rel="stylesheet" href="https://fonts.googleapis.com/css2?family=Open+Sans:wght@700;800&family=Raleway:wght@400;600;700&display=swap">
<style>
  :root {
    --bg: #e9e6e1;
    --card-white: #ffffff;
    --charcoal: #2a2929;
    --green: #8cc43c;
    --blue: #1b9ad8;
    --grey: #8f8f8f;
    --ink: #111111;
  }
  * { margin: 0; padding: 0; box-sizing: border-box; }
  html, body { width: 942px; height: 1200px; overflow: hidden; }
  body { background: var(--bg); position: relative; font-family: "Raleway", sans-serif; }

  .card {
    position: absolute;
    left: 93px;
    width: 718px;
    height: 434px;
    transform-origin: 0 0;
    transform: scale(1.0376);
    background: var(--card-white);
    box-shadow: 0 2px 6px rgba(0,0,0,.25);
    overflow: hidden;
  }
  .card--front { top: 106px; }
  .card--back { top: 637px; }
  .card__shapes { position: absolute; inset: 0; }

  .brand { position: absolute; display: flex; align-items: center; gap: 10px; }
  .brand__square { width: 16px; height: 16px; background: var(--charcoal); }
  .brand__name {
    font-family: "Raleway", sans-serif;
    font-weight: 700;
    font-size: 38px;
    color: var(--charcoal);
  }
  .card--front .brand { left: 44px; top: 176px; }
  .card--back .brand { left: 44px; top: 212px; }
  .card--back .brand__square { background: #ffffff; }
  .card--back .brand__name { color: #ffffff; }
  .brand-tagline {
    position: absolute; left: 46px; top: 276px;
    font-family: "Raleway", sans-serif; font-weight: 700;
    font-size: 16px; letter-spacing: 1px; color: #ffffff;
  }

  .contact { position: absolute; left: 344px; top: 52px; color: #ffffff; }
  .contact__name { font-weight: 700; font-size: 26px; margin-left: 22px; }
  .contact__title { font-weight: 400; font-size: 26px; margin-left: 16px; margin-top: 4px; }
  .contact__list { list-style: none; margin-top: 18px; }
  .contact__item { display: flex; align-items: center; gap: 8px; font-size: 21px; height: 33px; margin-left: 10px; }
  .contact__item svg { width: 18px; height: 18px; flex: none; }
  .contact__address { display: flex; gap: 8px; margin-top: 34px; margin-left: 2px; font-size: 21px; line-height: 27px; }
  .contact__address svg { width: 18px; height: 26px; flex: none; margin-top: 2px; }

  .pillars { position: absolute; left: 443px; top: 30px; width: 80px; text-align: center; }
  .pillar__label {
    font-family: "Open Sans", sans-serif; font-weight: 700; font-size: 23px;
    color: var(--charcoal); margin-left: -20px; margin-right: -20px; line-height: 30px;
  }
  .pillar__icon { width: 80px; height: 80px; display: block; margin: 6px 0 11px; }
</style>
</head>
<body>

<section class="card card--front" aria-label="Business card front">
  <svg class="card__shapes" viewBox="0 0 718 434" aria-hidden="true">
    <defs>
      <clipPath id="front-edge"><polygon points="715,0 718,0 718,434 665,434"/></clipPath>
    </defs>
    <polygon points="342,0 715,0 665,434 292,434" fill="var(--charcoal)"/>
    <g clip-path="url(#front-edge)" fill="var(--green)">
      <rect x="600" y="36" width="130" height="42"/>
      <rect x="600" y="104" width="130" height="42"/>
      <rect x="600" y="172" width="130" height="42"/>
      <rect x="600" y="240" width="130" height="42"/>
      <rect x="600" y="310" width="130" height="44"/>
      <rect x="600" y="380" width="130" height="54"/>
    </g>
  </svg>

  <div class="brand"><span class="brand__square"></span><span class="brand__name">Qbrook718</span></div>

  <div class="contact">
    <p class="contact__name">Tom Haskins</p>
    <p class="contact__title">CEO</p>
    <ul class="contact__list">
      <li class="contact__item">
        <svg viewBox="0 0 18 18"><rect x="4" y="1" width="10" height="16" rx="2" fill="none" stroke="#fff" stroke-width="1.5"/><line x1="7" y1="14" x2="11" y2="14" stroke="#fff" stroke-width="1.5"/></svg>
        123-456-7888
      </li>
      <li class="contact__item">
        <svg viewBox="0 0 18 18"><rect x="1" y="4" width="16" height="11" fill="none" stroke="#fff" stroke-width="1.5"/><polyline points="1,4 9,10 17,4" fill="none" stroke="#fff" stroke-width="1.5"/></svg>
        name@companyname.com
      </li>
      <li class="contact__item">
        <svg viewBox="0 0 18 18" fill="none" stroke="#fff" stroke-width="1.3"><circle cx="9" cy="9" r="7.5"/><ellipse cx="9" cy="9" rx="3.5" ry="7.5"/><line x1="1.5" y1="9" x2="16.5" y2="9"/><line x1="3" y1="5" x2="15" y2="5"/><line x1="3" y1="13" x2="15" y2="13"/></svg>
        www.companyname.com
      </li>
    </ul>
    <div class="contact__address">
      <svg viewBox="0 0 18 26"><path d="M9 1a8 8 0 0 0-8 8c0 6 8 16 8 16s8-10 8-16a8 8 0 0 0-8-8z" fill="#fff"/><circle cx="9" cy="9" r="3" fill="var(--charcoal)"/></svg>
      <p>2419 Pelkey Avenue<br>J7R-2B8<br>Montreal, Quebec</p>
    </div>
  </div>
</section>

<section class="card card--back" aria-label="Business card back">
  <svg class="card__shapes" viewBox="0 0 718 434" aria-hidden="true">
    <defs>
      <clipPath id="back-edge"><polygon points="712,0 718,0 718,434 665,434"/></clipPath>
    </defs>
    <polygon points="0,0 342,0 292,434 0,434" fill="var(--charcoal)"/>
    <g clip-path="url(#back-edge)">
      <rect x="600" y="0" width="130" height="434" fill="var(--green)"/>
      <g fill="var(--charcoal)">
        <rect x="600" y="0" width="130" height="24"/>
        <rect x="600" y="84" width="130" height="22"/>
        <rect x="600" y="154" width="130" height="22"/>
        <rect x="600" y="222" width="130" height="22"/>
        <rect x="600" y="292" width="130" height="22"/>
        <rect x="600" y="360" width="130" height="22"/>
      </g>
    </g>
  </svg>

  <div class="brand"><span class="brand__square"></span><span class="brand__name">Qbrook718</span></div>
  <p class="brand-tagline">Multi Channel Selling</p>

  <div class="pillars">
    <p class="pillar__label">SYNC</p>
    <svg class="pillar__icon" viewBox="0 0 80 80" aria-label="Computer icon" role="img">
      <circle cx="40" cy="40" r="40" fill="var(--blue)"/>
      <rect x="18" y="24" width="44" height="28" fill="var(--ink)"/>
      <rect x="21" y="27" width="38" height="22" fill="#fff"/>
      <rect x="37" y="52" width="6" height="6" fill="var(--ink)"/>
      <rect x="29" y="57" width="22" height="3" fill="var(--ink)"/>
    </svg>
    <p class="pillar__label">SELL</p>
    <svg class="pillar__icon" viewBox="0 0 80 80" aria-label="Money icon" role="img">
      <circle cx="40" cy="40" r="40" fill="var(--green)"/>
      <circle cx="40" cy="40" r="29" fill="#fff"/>
      <circle cx="40" cy="40" r="24" fill="none" stroke="var(--ink)" stroke-width="3"/>
      <text x="40" y="51" text-anchor="middle" font-family="Open Sans, sans-serif" font-weight="800" font-size="32" fill="var(--ink)">$</text>
    </svg>
    <p class="pillar__label">SHIP</p>
    <svg class="pillar__icon" viewBox="0 0 80 80" aria-label="Delivery van icon" role="img">
      <circle cx="40" cy="40" r="40" fill="var(--blue)"/>
      <path d="M14 30h36v22H14z M50 35h9l6 8v9H50z" fill="var(--ink)"/>
      <rect x="52" y="37" width="6" height="6" fill="var(--blue)"/>
      <circle cx="24" cy="53" r="5" fill="var(--ink)" stroke="var(--blue)" stroke-width="2"/>
      <circle cx="56" cy="53" r="5" fill="var(--ink)" stroke="var(--blue)" stroke-width="2"/>
      <g stroke="var(--ink)" stroke-width="2"><line x1="58" y1="28" x2="70" y2="28"/><line x1="60" y1="32" x2="70" y2="32"/></g>
    </svg>
  </div>
</section>

</body>
</html>
```